Company Real Estate Site Needs A Face Lift

I need a new website for the recent company I formed: Voska Real Estate.
You can use my agent website WWW.PALMIROQ.COM to see the style/brand I already have. I will have areas for Searching for homes on IDX, etc.
I really like this site:
http://www.cranfeltmanorhomes.com/
I have attached my logo as well

Industry/Entity Type

Real Estate

Colors
0255a3
ffffff
cee9f5

```html
<!DOCTYPE html>
<html lang="en">
<head>
<meta charset="utf-8">
<title>Voska Real Estate</title>
<link href="https://fonts.googleapis.com/css2?family=Open+Sans:wght@300;400;600;700&display=swap" rel="stylesheet">
<style>
:root{
  --brand:#0255a3;
  --brand-deep:#01427f;
  --brand-light:#1f7fcf;
  --ice:#cee9f5;
  --white:#ffffff;
  --ink:#2b2b2b;
  --heading:#4a4a4a;
  --muted:#9a9a9a;
  --footer:#ececec;
  --link:#444;
}
*{margin:0;padding:0;box-sizing:border-box}
html,body{width:870px;height:1200px;overflow:hidden;background:var(--white)}
body{position:relative;font-family:"Open Sans",Arial,sans-serif;color:var(--ink)}
.abs{position:absolute}
.header-band{left:0;top:0;width:870px;height:306px;background:var(--brand)}
.brand-mark{left:114px;top:26px;display:flex;align-items:center;gap:8px;color:var(--white);font-weight:700;font-size:18px;letter-spacing:.3px}
.brand-mark .dot{width:14px;height:14px;border-radius:50%;background:var(--ice)}
.contact{left:540px;top:43px;width:216px;text-align:right;color:var(--white);font-weight:700;font-size:10px;line-height:15px}
.main-nav{left:114px;top:78px;width:642px;height:38px;background:linear-gradient(#1a74c7,#0a5eae);display:flex;align-items:center;padding-left:26px;gap:22px}
.main-nav a{color:var(--white);font-weight:700;font-size:10px;text-decoration:none}
.photo{box-shadow:inset 0 0 0 1px rgba(0,0,0,.06)}
.hero{left:114px;top:116px;width:642px;height:247px;background:linear-gradient(180deg,#5f6f80 0%,#8f98a0 42%,#a77758 43%,#93644a 70%,#5d7046 71%,#7e8a6a 100%)}
.hero-dots{left:414px;top:340px;display:flex;gap:3px}
.hero-dots span{width:9px;height:9px;border-radius:50%;background:var(--white)}
.feature-img{top:410px;width:200px;height:95px}
.feature-title{top:524px;width:205px;font-weight:600;font-size:12px;line-height:16px;color:var(--heading)}
.feature-text{top:573px;width:210px;font-weight:300;font-size:9.1px;line-height:16px;color:var(--muted)}
.section-title{font-weight:700;font-size:12.5px;color:var(--ink)}
.video{left:120px;top:731px;width:361px;height:190px;background:linear-gradient(180deg,#a9c7e2 0%,#c9d6df 18%,#7d9868 19%,#6b8452 70%,#8a9078 100%)}
.video-bar{left:120px;top:925px;width:361px;height:16px;background:#1c1c1c}
.video-progress{left:120px;top:921px;width:361px;height:4px;background:#555}
.video-progress i{display:block;width:85px;height:4px;background:#d0201d}
.post-thumb{left:495px;width:94px;height:58px}
.post-date{left:495px;width:94px;text-align:center;font-size:7.5px;color:var(--ink)}
.post-text{left:595px;width:152px;font-weight:300;font-size:9.4px;line-height:16px;color:var(--muted)}
.footer{left:0;top:970px;width:870px;height:230px;background:var(--footer)}
.footer-title{top:990px;font-weight:700;font-size:9.5px;color:var(--ink)}
.footer-list{list-style:none;font-size:9.4px;line-height:19.3px;color:var(--link)}
.map{left:390px;top:1018px;width:199px;height:101px;background:#f1dc6a;border:1px solid #e2c94a}
.social{left:604px;top:1019px;display:flex;gap:4px}
.social span{width:27px;height:27px;border-radius:50%;background:var(--brand)}
.social span:nth-child(2){background:var(--brand-deep)}
.social span:nth-child(3){background:var(--brand-light)}
.badge{background:var(--white);border:2px solid var(--brand)}
.copyright{left:0;top:1168px;width:870px;text-align:center;font-size:9.5px;color:var(--ink)}
</style>
</head>
<body>
<div class="abs header-band"></div>
<div class="abs brand-mark"><span class="dot"></span>Voska Real Estate</div>
<div class="abs contact">CORIN VOSKA - 555-014-2290<br>CorinVoska@mailbox.example</div>
<nav class="abs main-nav">
  <a href="#">Home</a><a href="#">Search Homes</a><a href="#">Buy</a><a href="#">Sell</a><a href="#">Tours</a><a href="#">Testimonials</a><a href="#">Homes Blog</a><a href="#">Resources</a><a href="#">Contact</a>
</nav>
<div class="abs hero photo" role="img" aria-label="Brick family house with garage and garden under a cloudy sky"></div>
<div class="abs hero-dots"><span></span><span></span><span></span><span></span></div>

<div class="abs feature-img photo" style="left:120px;background:linear-gradient(180deg,#2a4a86 0%,#3a4a74 55%,#2b3a2a 100%)" role="img" aria-label="Large Tudor style home lit at dusk"></div>
<div class="abs feature-img photo" style="left:334px;background:linear-gradient(180deg,#b7c4cf 0%,#ece6d6 60%,#7d8f5a 100%)" role="img" aria-label="House with a sold sign in the front yard"></div>
<div class="abs feature-img photo" style="left:550px;background:linear-gradient(180deg,#e3e6ea 0%,#c3c6c8 62%,#86965f 100%)" role="img" aria-label="Family standing by a for sale sign outside a house"></div>

<h2 class="abs feature-title" style="left:120px">Charleston WV Real Estate &amp; Charleston WV Homes</h2>
<h2 class="abs feature-title" style="left:335px">Buying a Home?</h2>
<h2 class="abs feature-title" style="left:552px">Selling a Home?</h2>

<p class="abs feature-text" style="left:120px">Palmiroq.Com is designed to make your online research of the Charleston WV Real Estate /Hurricane WV Real Estate Market/Huntington WV Real Estate Market as “simple” as possible. My theory is that some people wish to remain anonymous, at first, when thinking of buying a home or selling Charleston WV Real Estate</p>
<p class="abs feature-text" style="left:335px">Whether you are a 1st time buyer or a home buying expert of Charleston WV Real Estate , you will be presented with many difficult choices that requires representation. If you want to avoid the pitfalls and aggravation often accompanied with buying</p>
<p class="abs feature-text" style="left:552px">Selling a home in Charleston WV/Hurricane WV/ Huntington WV entails more than just taking a few pictures, putting a “For Sale” sign in the yard and hoping something happens. Your invest-ment in me as your Realtor, ensures that you are being represented by me and not an assistant</p>

<h3 class="abs section-title" style="left:120px;top:706px">Featured Video</h3>
<div class="abs video photo" role="img" aria-label="Aerial view of a suburban neighbourhood"></div>
<svg class="abs" style="left:284px;top:810px" width="42" height="42" viewBox="0 0 42 42"><circle cx="21" cy="21" r="20" fill="#2a2a2a" fill-opacity=".8" stroke="#fff" stroke-width="1.5"/><path d="M16 12 L31 21 L16 30 Z" fill="#fff"/></svg>
<div class="abs video-progress"><i></i></div>
<div class="abs video-bar"></div>
<svg class="abs" style="left:130px;top:928px" width="340" height="10" viewBox="0 0 340 10"><rect x="3" y="1" width="2" height="8" fill="#ccc"/><rect x="7" y="1" width="2" height="8" fill="#ccc"/><path d="M28 3h3l4-3v10l-4-3h-3z" fill="#ccc"/><text x="46" y="8" font-size="6.5" fill="#fff" font-family="Open Sans,sans-serif">0:02 / 0:10</text><text x="296" y="8" font-size="6.5" fill="#ccc" font-family="Open Sans,sans-serif">720p</text><rect x="330" y="1" width="8" height="8" fill="none" stroke="#ccc"/></svg>

<h3 class="abs section-title" style="left:495px;top:706px">Recent Posts</h3>
<div class="abs post-thumb photo" style="top:738px;background:linear-gradient(180deg,#b3cde6 0%,#e3e4e0 55%,#5e8a3a 100%)" role="img" aria-label="Two storey country house on a lawn"></div>
<div class="abs post-date" style="top:803px">Feb 2,2014</div>
<p class="abs post-text" style="top:733px">Lorem Ipsum is simply dummy text of the printing and typesetting industry. Lorem Ipsum has been the industry's standard dummy text ever since the 1500s, when an unknown printer took a galley</p>
<div class="abs post-thumb photo" style="top:850px;background:linear-gradient(180deg,#1f4380 0%,#4a6ea6 55%,#1e3250 100%)" role="img" aria-label="Modern house by a pool at night"></div>
<div class="abs post-date" style="top:918px">Feb 2,2014</div>
<p class="abs post-text" style="top:845px">Lorem Ipsum is simply dummy text of the printing and typesetting industry. Lorem Ipsum has been the industry's standard dummy text ever since the 1500s, when an unknown printer took a galley</p>

<div class="abs footer"></div>
<h4 class="abs footer-title" style="left:121px">MLS NAVIGATION</h4>
<h4 class="abs footer-title" style="left:388px">LOCATION MAP</h4>
<h4 class="abs footer-title" style="left:605px">SOCIAL ICONS</h4>
<ul class="abs footer-list" style="left:123px;top:1025px">
  <li>Advanced Search</li><li>Map Search</li><li>Address Search</li><li>Our Featured Listings</li><li>Listing Manager Login</li><li>Email Updates Signup</li>
</ul>
<ul class="abs footer-list" style="left:278px;top:1028px">
  <li>&nbsp;Listing ID Search</li><li>Open Houses</li><li>Sold/Pending Listings</li><li>Home Valuation Request</li><li>IDX/MLS Sitemap</li><li>Search by City</li>
</ul>
<div class="abs map" role="img" aria-label="Street map of the office location with markers"></div>
<div class="abs social"><span></span><span></span><span></span></div>
<div class="abs badge" style="left:608px;top:1056px;width:115px;height:22px;border-radius:11px"></div>
<div class="abs badge" style="left:611px;top:1086px;width:71px;height:38px;border-radius:4px"></div>
<div class="abs badge" style="left:694px;top:1090px;width:36px;height:34px;border-radius:4px"></div>
<div class="abs copyright">© 2014 Company Name ,All Rights Reserved</div>
</body>
</html>
```